TWR Business Card Design

As a full service media and advocacy firm, we lean on years of experience in political and corporate consulting, grassroots campaigning, media placement, and video production to deliver unparalleled results. Recently we have moved into digital media and now provide this service for our clients.

I will add our two company logos to be used on the business cards. The longer logo with "sky reach studio" is our primary logo. Our secondary logo is more square one with "sky reach" and 'digital.media.campaigns" on it. We are looking for clean and modern looking business cards fitting for a digital firm.

I will also add our logos that go well with dark backgrounds.

Industry/Entity Type

Political

Contact Information for Business Card

Walter Pennick, Director of Campaigns and Digital, 555-218-4760, walter@skyreachstudioco.example, @SkyReachStudioCo, @WalterPennick, Facebook.com/SkyReachStudioCo

```html
<!DOCTYPE html>
<html lang="en">
<head>
<meta charset="utf-8">
<title>TWR Business Card</title>
<link rel="stylesheet" href="https://fonts.googleapis.com/css2?family=Open+Sans:wght@400;600&display=swap">
<style>
  :root {
    --stage: #1b1b1c;
    --card: #2a2a2c;
    --card-edge: #323235;
    --ink: #e9e9ea;
    --ink-soft: #c9c9cc;
    --blue: #2c8fd6;
    --blue-deep: #2e5fc0;
    --gloss: #141415;
  }
  * { margin: 0; padding: 0; box-sizing: border-box; }
  html, body { width: 1200px; height: 716px; overflow: hidden; }
  body {
    background: var(--stage);
    font-family: "Open Sans", Arial, sans-serif;
    position: relative;
  }
  .card {
    position: absolute;
    top: 210px;
    width: 520px;
    height: 297px;
    background: var(--card);
    border: 1px solid var(--card-edge);
    border-radius: 3px;
  }
  .card-front { left: 50px; }
  .card-back { left: 630px; }

  .front-brand {
    position: absolute;
    inset: 0;
    display: flex;
    align-items: center;
    justify-content: center;
    gap: 12px;
  }
  .front-brand .brand-name {
    font-size: 44px;
    font-weight: 600;
    letter-spacing: 2px;
    color: var(--gloss);
  }
  .front-brand .brand-dot {
    width: 14px; height: 14px; border-radius: 50%;
    background: var(--gloss);
  }

  .back-brand {
    position: absolute;
    top: 26px;
    right: 26px;
    display: flex;
    align-items: center;
    gap: 8px;
  }
  .back-brand .brand-name {
    font-size: 26px;
    font-weight: 600;
    letter-spacing: 1px;
    color: var(--blue-deep);
  }
  .back-brand .brand-dot {
    width: 9px; height: 9px; border-radius: 50%;
    background: var(--blue-deep);
  }

  .holder {
    position: absolute;
    left: 28px;
    top: 92px;
  }
  .holder-name {
    font-size: 17px;
    font-weight: 600;
    letter-spacing: 1.5px;
    color: var(--blue);
    text-transform: uppercase;
  }
  .holder-title {
    font-size: 11px;
    color: var(--ink);
    margin-top: 2px;
  }
  .rule {
    position: absolute;
    left: 22px;
    right: 22px;
    top: 140px;
    height: 1px;
    background: var(--blue);
  }

  .contact-list {
    position: absolute;
    left: 28px;
    top: 158px;
    list-style: none;
  }
  .contact-list li,
  .social-list li {
    display: flex;
    align-items: center;
    gap: 7px;
    font-size: 11px;
    line-height: 19px;
    color: var(--ink-soft);
  }
  .contact-list .plain { padding-left: 19px; }
  .icon {
    width: 12px; height: 12px;
    flex: none;
  }
  .social-list {
    position: absolute;
    right: 30px;
    top: 210px;
    list-style: none;
  }
  .social-mark {
    width: 11px; height: 11px;
    border-radius: 2px;
    background: var(--blue);
    flex: none;
  }
</style>
</head>
<body>

<section class="card card-front" aria-label="Card front">
  <div class="front-brand">
    <span class="brand-name">SKY REACH</span>
    <span class="brand-dot"></span>
  </div>
</section>

<section class="card card-back" aria-label="Card back">
  <div class="back-brand">
    <span class="brand-name">SKY REACH</span>
    <span class="brand-dot"></span>
  </div>

  <div class="holder">
    <p class="holder-name">Walter Pennick</p>
    <p class="holder-title">Director of Campaigns and Digital</p>
  </div>

  <div class="rule"></div>

  <ul class="contact-list">
    <li>
      <svg class="icon" viewBox="0 0 12 12" aria-hidden="true">
        <rect width="12" height="12" rx="2" fill="var(--blue)"/>
        <path d="M3.6 2.6 L5 4.4 L4.3 5.2 Q5.2 6.9 6.8 7.7 L7.6 7 L9.4 8.4 L8.6 9.5 Q4.8 9 2.6 3.5 Z" fill="var(--card)"/>
      </svg>
      555-218-4760
    </li>
    <li>
      <svg class="icon" viewBox="0 0 12 12" aria-hidden="true">
        <rect width="12" height="12" rx="2" fill="var(--blue)"/>
        <rect x="2.5" y="3.5" width="7" height="5" fill="none" stroke="var(--card)" stroke-width="1"/>
        <path d="M2.5 3.5 L6 6.3 L9.5 3.5" fill="none" stroke="var(--card)" stroke-width="1"/>
      </svg>
      walter@skyreachstudioco.example
    </li>
    <li class="plain">www.skyreachstudioco.example</li>
  </ul>

  <ul class="social-list">
    <li><span class="social-mark"></span>@SkyReachStudioCo</li>
    <li><span class="social-mark"></span>@WalterPennick</li>
    <li><span class="social-mark"></span>/SkyReachStudioCo</li>
  </ul>
</section>

</body>
</html>
```